Vormace

I need a professional web site that is directed at the energy industry, Oil, Gas, Mining
I need the website to have the usual pages
1. home page
2. news page.
3. contact us page
4. About us
and a CMS admin section to add further pages and content
Must be Google friendly with SEO facility

Target Market(s)

energy industry, Oil, Gas, Mining

Industry/Entity Type

Industry

Font styles to use
Sans Serif

Colors
faa54b
85cae6
cadf82

Requirements
Must have
• social media icons
site map

```html
<!DOCTYPE html>
<html lang="en">
<head>
<meta charset="utf-8">
<title>Vormace – Mining, Oil &amp; Gas</title>
<link href="https://fonts.googleapis.com/css2?family=Open+Sans:ital,wght@0,400;0,600;0,700;0,800;1,600&display=swap" rel="stylesheet">
<style>
:root{
  --orange:#f7931e;
  --orange-dark:#a8641f;
  --ink:#2e2e2e;
  --text:#666;
  --white:#fff;
  --dark:#1b1b1b;
  --rule:#ececec;
}
*{box-sizing:border-box;margin:0;padding:0}
html,body{width:1200px;height:2446px;overflow:hidden}
body{font-family:"Open Sans",Arial,sans-serif;color:var(--ink);background:var(--white);position:relative}
.abs{position:absolute}
.btn{position:absolute;background:var(--orange);color:var(--white);font-weight:600;font-size:14px;text-transform:uppercase;display:flex;align-items:center;justify-content:center;height:41px;letter-spacing:.2px}

/* hero */
.hero{position:absolute;left:0;top:0;width:1200px;height:478px;background:radial-gradient(ellipse at 45% 40%,#4a4232 0%,#2a2620 45%,#141311 100%)}
.hero-photo{position:absolute;inset:0;background:linear-gradient(180deg,rgba(0,0,0,.15),rgba(0,0,0,.35)),radial-gradient(ellipse at 40% 35%,rgba(150,130,60,.35),transparent 45%)}
.logo{position:absolute;top:26px;left:0;width:1200px;text-align:center;color:var(--white);font-weight:800;font-size:30px;letter-spacing:1px}
.nav{position:absolute;left:176px;top:82px;width:848px;height:42px;background:var(--orange);color:var(--white);font-size:11px;font-weight:600;text-transform:uppercase}
.nav span{position:absolute;top:13px}
.nav .contact{text-transform:none;display:flex;align-items:center;gap:6px}
.hero h1{position:absolute;top:192px;width:1200px;text-align:center;color:var(--white);font-size:32px;font-weight:600;line-height:37px}
.dots{position:absolute;top:435px;left:535px;display:flex;gap:3px}
.dots i{display:block;width:31px;height:3px;background:var(--white)}
.dots i:first-child{background:var(--orange)}

/* section headings */
.heading{position:absolute;left:0;width:1200px;display:flex;justify-content:center;align-items:center;gap:10px;font-size:32px;font-weight:700;text-transform:uppercase}
.heading::before,.heading::after{content:"";width:130px;height:7px;background:var(--rule)}
.heading.dark{color:var(--white)}
.heading.dark::before,.heading.dark::after{background:var(--orange-dark)}

/* welcome */
.lead{font-size:21px;font-weight:700;line-height:26px;text-transform:uppercase}
.body{font-size:12px;line-height:20px;color:var(--text)}
.bignum{font-size:96px;font-weight:700;line-height:1;letter-spacing:-3px}
.bignum b{color:var(--orange)}
.sub{font-size:13px;font-weight:700;color:var(--orange);text-transform:uppercase}

/* services */
.services{position:absolute;left:0;top:949px;width:1200px;height:453px;background:linear-gradient(180deg,#1f1f1f,#141414 70%,#232323)}
.service-img{position:absolute;top:111px;width:256px;height:123px}
.service h3{position:absolute;top:252px;width:256px;text-align:center;color:var(--white);font-size:21px;font-weight:700}
.service p{position:absolute;top:288px;width:256px;text-align:center;color:#ddd;font-size:12px;line-height:20px}

/* news */
.meta{font-size:11px;color:var(--orange);display:flex;align-items:center;gap:5px}
.readmore{color:var(--orange)}

/* testimonials */
.testimonials{position:absolute;left:0;top:1902px;width:1200px;height:361px;background:radial-gradient(ellipse at 50% 40%,#4a4440,#262221 70%,#1a1716)}
.quote{position:absolute;top:242px;left:265px;width:670px;text-align:center;color:var(--white);font-size:11px;line-height:20px}
.author{position:absolute;top:310px;width:1200px;text-align:center;color:var(--orange);font-size:12px;font-weight:600;font-style:italic}

/* footer */
.social{position:absolute;top:2307px;left:0;width:1200px;display:flex;justify-content:center;gap:20px}
.social i{display:block;width:42px;height:42px;border-radius:50%;background:#1e1e1e}
.copyright{position:absolute;top:2382px;width:1200px;text-align:center;font-size:14px;color:#333}
</style>
</head>
<body>

<header class="hero">
  <div class="hero-photo" role="img" aria-label="Photo of a large yellow mining dump truck at a dusty open-pit site"></div>
  <div class="logo">VORMACE</div>
  <nav class="nav">
    <span style="left:15px">Home</span>
    <span style="left:80px">About Us</span>
    <span style="left:167px">Our Services</span>
    <span style="left:274px">Latest News</span>
    <span style="left:378px">Contact Us</span>
    <span class="contact" style="left:585px">
      <svg width="10" height="10" viewBox="0 0 24 24"><path fill="#fff" d="M6.6 10.8a15 15 0 0 0 6.6 6.6l2.2-2.2a1 1 0 0 1 1-.25 11.4 11.4 0 0 0 3.6.6 1 1 0 0 1 1 1V20a1 1 0 0 1-1 1A17 17 0 0 1 3 4a1 1 0 0 1 1-1h3.5a1 1 0 0 1 1 1c0 1.25.2 2.45.6 3.6a1 1 0 0 1-.25 1z"/></svg>
      + 1 555 014 2290</span>
    <span class="contact" style="left:715px">
      <svg width="11" height="9" viewBox="0 0 22 16"><rect width="22" height="16" rx="2" fill="#fff"/><path d="M1 1l10 8 10-8" stroke="#f7931e" stroke-width="2" fill="none"/></svg>
      info@vormace.com</span>
  </nav>
  <h1>THE LEADER IN MINING COMPANY<br>IN THE WORLD</h1>
  <div class="btn" style="left:520px;top:295px;width:160px">Explore Service</div>
  <div class="dots"><i></i><i></i><i></i><i></i></div>
</header>

<section class="welcome">
  <h2 class="heading" style="top:510px">Welcome to Vormace</h2>
  <div class="abs lead" style="left:176px;top:600px">We are<br>competitive in<br>our services</div>
  <p class="abs body" style="left:176px;top:700px;width:300px">The generated Lorem Ipsum is therefore alwa free from repetition, injected humour, or non-characteristic words etc.</p>
  <p class="abs body" style="left:176px;top:778px;width:300px">Sque dolor nisl,ellentesque dolor nisl, laoreet in pellentesque eget, laoreet a eros.</p>
  <div class="btn" style="left:176px;top:851px;width:132px">View Service</div>

  <div class="abs bignum" style="left:522px;top:604px">01<b>.</b></div>
  <div class="abs sub" style="left:528px;top:703px">Our History</div>
  <p class="abs body" style="left:528px;top:724px;width:210px">Sedquis viverra enim. Vivamus aliquet rutrum dui a varius. Mauris ornare tortor in eleifend blanditullam ut ligula et neque. Lorem Ipsum is therefore alwa free from repetition</p>
  <div class="btn" style="left:528px;top:851px;width:132px">Read More</div>

  <div class="abs bignum" style="left:788px;top:604px">02<b>.</b></div>
  <div class="abs sub" style="left:794px;top:703px">Our Vision &amp; Mission</div>
  <p class="abs body" style="left:794px;top:724px;width:210px">Sedquis viverra enim. Vivamus aliquet rutrum dui a varius. Mauris ornare tortor in eleifend blanditullam ut ligula et neque. Lorem Ipsum is therefore alwa free from repetition</p>
  <div class="btn" style="left:794px;top:851px;width:132px">Read More</div>
</section>

<section class="services">
  <h2 class="heading dark" style="top:38px">Our Services</h2>
  <div class="service">
    <div class="service-img" style="left:176px;background:linear-gradient(180deg,#3c5a80 0%,#c99a6a 50%,#2a2a30 60%,#7a6650 100%)" role="img" aria-label="Oil refinery lit at dusk reflected in water"></div>
    <h3 style="left:176px">OIL</h3>
    <p style="left:176px">Sedquis viverra enim. Vivamus aliquet rutrum dui a varius. Mauris ornare tortor in eleifend blanditullam ut ligula et neque.</p>
    <div class="btn" style="left:238px;top:370px;width:132px">Read More</div>
  </div>
  <div class="service">
    <div class="service-img" style="left:473px;background:linear-gradient(135deg,#1f3a5a,#8fb6d4 45%,#d9e6ee 55%,#3a5a78)" role="img" aria-label="Close-up of blue steel gas pipelines"></div>
    <h3 style="left:473px">GAS</h3>
    <p style="left:473px">Sedquis viverra enim. Vivamus aliquet rutrum dui a varius. Mauris ornare tortor in eleifend blanditullam ut ligula et neque.</p>
    <div class="btn" style="left:535px;top:370px;width:132px">Read More</div>
  </div>
  <div class="service">
    <div class="service-img" style="left:768px;background:linear-gradient(160deg,#a89878,#7a6a52 60%,#c8a040)" role="img" aria-label="Yellow mining trucks and excavator at a quarry"></div>
    <h3 style="left:768px">MINING</h3>
    <p style="left:768px">Sedquis viverra enim. Vivamus aliquet rutrum dui a varius. Mauris ornare tortor in eleifend blanditullam ut ligula et neque.</p>
    <div class="btn" style="left:830px;top:370px;width:132px">Read More</div>
  </div>
</section>

<section class="news">
  <h2 class="heading" style="top:1440px">Latest News</h2>

  <div class="abs bignum" style="left:172px;top:1530px">01<b>.</b></div>
  <div class="abs meta" style="left:176px;top:1632px"><svg width="10" height="10" viewBox="0 0 10 10"><rect x=".5" y="1.5" width="9" height="8" fill="none" stroke="#f7931e"/><rect x=".5" y="1.5" width="9" height="2.5" fill="#f7931e"/></svg>30-12-2014</div>
  <p class="abs body" style="left:176px;top:1660px;width:262px">Sedquis viverra enim. Vivamus aliquet rutrum dusi a varius. Mauris ornare tortor in eleifend blanditullam ut ligula et neque. Lorem Ipsum is therefore alwa free from repetition <span class="readmore">Read More...</span></p>
  <div class="abs meta" style="left:176px;top:1754px"><svg width="10" height="10" viewBox="0 0 10 10"><path d="M0 0h5l5 5-5 5-5-5z" fill="#f7931e"/></svg>Mining Industry</div>
  <div class="abs meta" style="left:347px;top:1754px"><svg width="10" height="10" viewBox="0 0 10 10"><circle cx="5" cy="5" r="5" fill="#f7931e"/></svg>05 Comments</div>

  <div class="abs bignum" style="left:474px;top:1530px">02<b>.</b></div>
  <div class="abs meta" style="left:478px;top:1632px"><svg width="10" height="10" viewBox="0 0 10 10"><rect x=".5" y="1.5" width="9" height="8" fill="none" stroke="#f7931e"/><rect x=".5" y="1.5" width="9" height="2.5" fill="#f7931e"/></svg>30-12-2014</div>
  <p class="abs body" style="left:478px;top:1660px;width:262px">Sedquis viverra enim. Vivamus aliquet rutrum dusi a varius. Mauris ornare tortor in eleifend blanditullam ut ligula et neque. Lorem Ipsum is therefore alwa free from repetition <span class="readmore">Read More...</span></p>
  <div class="abs meta" style="left:478px;top:1754px"><svg width="10" height="10" viewBox="0 0 10 10"><path d="M0 0h5l5 5-5 5-5-5z" fill="#f7931e"/></svg>Mining Industry</div>
  <div class="abs meta" style="left:649px;top:1754px"><svg width="10" height="10" viewBox="0 0 10 10"><circle cx="5" cy="5" r="5" fill="#f7931e"/></svg>05 Comments</div>

  <div class="abs bignum" style="left:761px;top:1530px">03<b>.</b></div>
  <div class="abs meta" style="left:765px;top:1632px"><svg width="10" height="10" viewBox="0 0 10 10"><rect x=".5" y="1.5" width="9" height="8" fill="none" stroke="#f7931e"/><rect x=".5" y="1.5" width="9" height="2.5" fill="#f7931e"/></svg>30-12-2014</div>
  <p class="abs body" style="left:765px;top:1660px;width:262px">Sedquis viverra enim. Vivamus aliquet rutrum dusi a varius. Mauris ornare tortor in eleifend blanditullam ut ligula et neque. Lorem Ipsum is therefore alwa free from repetition <span class="readmore">Read More...</span></p>
  <div class="abs meta" style="left:765px;top:1754px"><svg width="10" height="10" viewBox="0 0 10 10"><path d="M0 0h5l5 5-5 5-5-5z" fill="#f7931e"/></svg>Mining Industry</div>
  <div class="abs meta" style="left:928px;top:1754px"><svg width="10" height="10" viewBox="0 0 10 10"><circle cx="5" cy="5" r="5" fill="#f7931e"/></svg>05 Comments</div>

  <div class="btn" style="left:527px;top:1814px;width:146px">Read All News</div>
</section>

<section class="testimonials" role="region" aria-label="Client testimonials">
  <div class="abs" style="inset:0" role="img" aria-label="Blurred crowd of people in the background"></div>
  <h2 class="heading dark" style="top:36px">Client Testimonials</h2>
  <div class="abs" style="left:545px;top:105px;width:110px;height:110px;border-radius:50%;border:3px solid #ddd;background:radial-gradient(circle at 50% 40%,#c9a58a,#6a4a38)" role="img" aria-label="Portrait of the client"></div>
  <svg class="abs" style="left:188px;top:158px" width="24" height="44" viewBox="0 0 24 44"><path d="M22 2L2 22l20 20" stroke="#fff" stroke-width="1.5" fill="none"/></svg>
  <svg class="abs" style="left:986px;top:158px" width="24" height="44" viewBox="0 0 24 44"><path d="M2 2l20 20L2 42" stroke="#fff" stroke-width="1.5" fill="none"/></svg>
  <p class="quote">Sed leo libero, tempor in volutpat et, vehicula sit amet mauris. Mauris ut luctus massa. Pellentesque suscipit sit amet dolor maximus porttitor. Nullam porttitor consectetur sem id viverra. Aenean turpis enim, pretium nec odio nec, ornare convallis arcu. Quisque vehicula purus vel quam commodo, sed cursus ex egestas.</p>
  <div class="author">- Daniel Harlow</div>
</section>

<footer>
  <div class="social" aria-label="Social media links"><i></i><i></i><i></i><i></i><i></i></div>
  <p class="copyright">Copyright ©2014 Vormace. All Rights Reserved. Designed by Fenwick Studio</p>
</footer>

</body>
</html>
```